VOIP company busioness card redesign

Redesign business card to match our new logo and marketing material. Should include logo on one side and contact information on other side.

We like modern and clean

Industry/Entity Type

Phone Company

Contact Information for Business Card

One side should be logo other side should include contact info
Name
Phone Number
email
website

Other font styles liked:
• dont care

Requirements
Must have
• Modern sleek design that works with our logo

```html
<!DOCTYPE html>
<html lang="en">
<head>
<meta charset="utf-8">
<title>Nimbara Solutions – Business Card</title>
<link href="https://fonts.googleapis.com/css2?family=Lato:wght@400;700;900&display=swap" rel="stylesheet">
<style>
  :root {
    --stage: #222222;
    --brand-blue: #0b9fda;
    --brand-green: #7ab834;
    --text-grey: #8d8d8d;
    --rule-grey: #c9c9c9;
    --paper: #ffffff;
  }
  * { box-sizing: border-box; margin: 0; padding: 0; }
  html, body {
    width: 1189px; height: 1200px; overflow: hidden;
    background: var(--stage);
    font-family: "Lato", sans-serif;
  }
  .card {
    position: absolute;
    left: 171px;
    width: 856px;
    height: 487px;
    border-radius: 26px;
    box-shadow: 0 10px 22px rgba(0,0,0,0.6);
  }
  .card--front { top: 68px; background: var(--brand-blue); }
  .card--back  { top: 627px; background: var(--paper); }

  .wordmark, .tagline {
    position: absolute;
    line-height: 1;
    white-space: nowrap;
  }

  /* front: wordmark lockup */
  .card--front .wordmark {
    left: 157px; top: 195px;
    font-weight: 900; font-size: 118px; letter-spacing: -2px;
    color: var(--paper);
  }
  .card--front .tagline {
    left: 311px; top: 310px;
    font-weight: 400; font-size: 23px; letter-spacing: 0.3px;
    color: var(--paper);
  }

  /* back: wordmark left */
  .card--back .wordmark {
    left: 42px; top: 211px;
    font-weight: 900; font-size: 80px; letter-spacing: -1px;
    color: var(--brand-blue);
  }
  .card--back .tagline {
    left: 142px; top: 289px;
    font-size: 15.5px;
    color: var(--text-grey);
  }

  .divider {
    position: absolute; left: 431px; top: 111px;
    width: 2px; height: 266px; background: var(--rule-grey);
  }

  .contact { position: absolute; left: 466px; top: 110px; }
  .contact .person-name {
    color: var(--brand-blue); font-weight: 700; font-size: 30px; line-height: 1;
  }
  .contact .person-role {
    color: var(--brand-green); font-size: 24px; line-height: 1.1;
  }
  .contact .address {
    color: var(--text-grey); font-size: 24px; line-height: 30px; margin-top: 50px;
  }
  .contact-list { list-style: none; margin-top: 12px; }
  .contact-list li {
    display: flex; align-items: center; gap: 9px;
    color: var(--text-grey); font-size: 24px; height: 30px;
  }
  .contact-icon {
    width: 27px; height: 27px; border-radius: 3px;
    background: var(--brand-green);
    display: flex; align-items: center; justify-content: center;
    flex: none;
  }
</style>
</head>
<body>

<section class="card card--front" aria-label="Card front">
  <div class="wordmark">Nimbara</div>
  <div class="tagline">Business Voice Made Effortless</div>
</section>

<section class="card card--back" aria-label="Card back">
  <div class="wordmark">Nimbara</div>
  <div class="tagline">Business Voice Made Effortless</div>

  <div class="divider"></div>

  <div class="contact">
    <p class="person-name">DANA MARLOW</p>
    <p class="person-role">Chief Executive Officer</p>
    <p class="address">100 Harbor Way, Ste 2<br>Fairview, Texas 1234</p>
    <ul class="contact-list">
      <li>
        <span class="contact-icon">
          <svg width="17" height="17" viewBox="0 0 24 24"><path fill="#fff" d="M6.6 10.8a15.1 15.1 0 0 0 6.6 6.6l2.2-2.2a1 1 0 0 1 1-.25 11.4 11.4 0 0 0 3.6.6 1 1 0 0 1 1 1V20a1 1 0 0 1-1 1A17 17 0 0 1 3 4a1 1 0 0 1 1-1h3.5a1 1 0 0 1 1 1c0 1.25.2 2.45.6 3.6a1 1 0 0 1-.25 1z"/></svg>
        </span>
        123 456 7890
      </li>
      <li>
        <span class="contact-icon">
          <svg width="18" height="14" viewBox="0 0 18 14"><rect x="1" y="1" width="16" height="12" fill="none" stroke="#fff" stroke-width="1.6"/><path d="M1 1l8 6 8-6M1 13l6-5M17 13l-6-5" fill="none" stroke="#fff" stroke-width="1.4"/></svg>
        </span>
        your@yourcompany.com
      </li>
      <li>
        <span class="contact-icon">
          <svg width="18" height="18" viewBox="0 0 20 20" fill="none" stroke="#fff" stroke-width="1.4"><circle cx="10" cy="10" r="8"/><ellipse cx="10" cy="10" rx="3.5" ry="8"/><path d="M2 10h16M3.5 6h13M3.5 14h13"/></svg>
        </span>
        www.yourcompany.com
      </li>
    </ul>
  </div>
</section>

</body>
</html>
```